WordPress Website Design - Brennick Auction

Need a WordPress design for an auction company wanting a responsive, simple and easy to use site. Current site to be upgraded: http://www.brennickauctions.example/

A site the client mentions liking is http://www.taverlyauction.example. The attached logo color can be changed to suit your design - a different red, or green perhaps.

Industry/Entity Type

It Company

Number of Pages Required

1 page

Font styles to use
Serif
Sans Serif

Requirements
Must have
• Keep in mind this site will be built on a responsive theme.
• Site navigation: 1) Home, 2) Auctions, 3) Real Estate Listings, 4) Services, 5) Appraisals, 6) The Gavel Hall, 7) About Us, 8) Contact Us
• Site will have large, prominent full width (960px) slideshow - please pick one of the 3 attached images. Colors can be different than current site - wants a brighter site, colors complementing the logo. Home page will have auction list (the look of the auction list can be seen at http://www.northgateholdingsweb.example/auction-calendar/)
• The widgets in the sidebar/header are: Email signup form, social media(FB Twitter, Youtube), News & Events blog, Testimonials, Featured Auctions, Featured Listings widget.
• Footer will have smaller company logo(below), contact info, and attached association logos.
• Gordon Brennick Auction-Realty
• 3817 Pelham Court • Castor Falls, IN 47088
• dominic@brennickauctions.example
• 812.555.0146
• 877.555.0193
Nice to have
• Design of dropdown menus: under Auctions, 1) Current Auctions, 2) Online Auctions, 3) Past Auctions

```html
<!DOCTYPE html>
<html lang="en">
<head>
<meta charset="utf-8">
<title>Brennick Auction</title>
<link href="https://fonts.googleapis.com/css2?family=Open+Sans:wght@400;600;700;800&display=swap" rel="stylesheet">
<style>
:root{
  --red:#e2404f;
  --nav:#3b3b3d;
  --page:#eeeeee;
  --card:#ffffff;
  --ink:#333333;
  --muted:#777777;
  --footer:#2a2a2c;
  --footer-deep:#1f1f21;
  --line:#dddddd;
}
*{box-sizing:border-box;margin:0;padding:0}
html,body{width:1200px;height:3116px;overflow:hidden}
body{font-family:"Open Sans",Arial,sans-serif;color:var(--ink);background:var(--page);position:relative}
.site-header{height:100px;background:#fff;position:relative}
.brand{position:absolute;left:40px;top:30px;display:flex;align-items:center;gap:10px;font-size:30px;font-weight:800;color:var(--ink);letter-spacing:-.5px}
.brand::after{content:"";width:14px;height:14px;border-radius:50%;background:var(--red)}
.header-social{position:absolute;right:36px;top:18px;display:flex;gap:10px}
.header-social i{width:26px;height:26px;border-radius:50%;background:var(--red);display:block}
.header-social i:nth-child(2){background:#bbb}
.main-nav{position:absolute;top:100px;left:0;width:1200px;height:34px;background:var(--nav);display:flex;padding-left:36px;z-index:2}
.main-nav a{color:#fff;font-size:12px;text-decoration:none;padding:0 22px;line-height:34px;font-weight:600}
.main-nav a.active{background:var(--red)}
.hero{position:absolute;top:134px;left:0;width:1200px;height:526px;background:linear-gradient(180deg,#9fb8d6 0%,#cbd7e0 38%,#7d8a6a 62%,#5b6050 80%,#8a8a86 100%)}
.hero-offer{position:absolute;right:20px;top:210px;width:410px;height:236px;background:rgba(226,64,79,.88);color:#fff;padding:26px 28px;text-align:right}
.hero-offer h1{font-size:30px;font-weight:800;line-height:1.15;text-transform:uppercase}
.hero-offer p{font-size:12px;margin-top:12px;line-height:1.5}
.btn{display:inline-block;background:#fff;color:var(--ink);font-size:11px;font-weight:700;padding:9px 16px;margin-top:16px;text-transform:uppercase}
.section-title{position:absolute;left:32px;top:724px;color:var(--red);font-size:20px;font-weight:700;text-transform:uppercase;display:flex;align-items:center;gap:8px}
.section-title::after{content:"";position:absolute;left:0;right:0;bottom:-8px;height:2px;background:var(--red)}
.auction-grid{position:absolute;left:32px;top:800px;width:750px;display:grid;grid-template-columns:360px 360px;gap:28px 30px}
.auction-card{background:var(--card);height:420px;padding:14px 16px}
.auction-card .tag{color:var(--red);font-size:11px;font-weight:700;text-align:center;text-transform:uppercase}
.auction-card .thumb{height:148px;margin-top:10px;background:linear-gradient(180deg,#8fb3d9 0%,#c8d4dd 45%,#b9aa90 60%,#6d7d55 100%)}
.auction-card:nth-child(2n) .thumb{background:linear-gradient(180deg,#9cc0e2 0%,#e9e4da 50%,#9a8a72 70%,#5f7448 100%)}
.auction-card h3{font-size:14px;margin-top:14px;font-weight:600}
.auction-card .desc{font-size:11px;color:var(--muted);line-height:1.5;margin-top:6px}
.meta{display:flex;gap:8px;font-size:11px;margin-top:12px;line-height:1.5}
.meta svg{flex:none;margin-top:2px}
.meta b{width:62px;flex:none}
.sidebar{position:absolute;left:812px;top:800px;width:356px}
.widget{background:var(--card);margin-bottom:26px}
.widget h4{background:var(--red);color:#fff;font-size:14px;font-weight:600;padding:10px 16px}
.widget .body{padding:14px 16px;font-size:11px;color:var(--muted);line-height:1.5}
.field{height:28px;background:#f3f3f3;border:1px solid var(--line);margin-top:10px}
.subscribe{margin:10px auto 0;width:140px;height:26px;background:#888;color:#fff;font-size:10px;font-weight:700;text-align:center;line-height:26px}
.social-row{display:flex;justify-content:center;gap:14px}
.social-row span{width:60px;height:44px;background:var(--red);color:#fff;font-size:11px;font-weight:700;text-align:center;line-height:44px;text-transform:uppercase}
.item{display:flex;gap:12px;margin-bottom:12px}
.date{width:46px;height:46px;background:var(--red);color:#fff;font-size:12px;font-weight:700;text-align:center;line-height:1.2;padding-top:6px;flex:none}
.avatar{width:52px;height:52px;background:linear-gradient(160deg,#c9b6a4,#7c6b60);flex:none}
.item strong{display:block;color:var(--ink);font-size:12px}
.view-all{text-align:right;font-size:10px;color:var(--red);font-weight:600}
.pics{display:flex;gap:12px}
.pics div{flex:1;height:84px;background:linear-gradient(180deg,#a9c4dd,#dcd6c8 55%,#6e8352)}
.brand-band{position:absolute;top:2620px;left:0;width:1200px;height:226px;background:#fff}
.brand-band .brand{position:static;justify-content:center;padding-top:26px;font-size:30px}
.partners{display:flex;justify-content:center;gap:34px;margin-top:36px}
.partners i{width:130px;height:64px;border:1px solid var(--line);display:block;background:#f5f5f5}
.partners i::after{content:"";display:block;width:44px;height:44px;background:#cfcfcf;margin:9px auto}
.site-footer{position:absolute;top:2846px;left:0;width:1200px;height:270px;background:var(--footer);color:#fff}
.contacts{display:flex;justify-content:space-around;padding:60px 90px 0;font-size:20px;font-weight:600}
.contacts span{display:flex;align-items:center;gap:12px}
.address{margin-top:44px;text-align:center;font-size:14px}
.address b{color:var(--red);margin-right:14px}
.legal{position:absolute;bottom:0;left:0;right:0;height:46px;background:var(--footer-deep);color:#888;font-size:11px;text-align:center;line-height:46px}
</style>
</head>
<body>
<header class="site-header">
  <div class="brand">brennickauctions.example</div>
  <div class="header-social"><i></i><i></i></div>
</header>
<nav class="main-nav">
  <a class="active">Home</a><a>Auctions</a><a>Real Estate Listings</a><a>Services</a><a>Appraisals</a><a>The Gavel Hall</a><a>About Us</a><a>Contact Us</a>
</nav>
<section class="hero" role="img" aria-label="Photo of a two-storey house with a green lawn and driveway">
  <div class="hero-offer">
    <h1>Lorem ipsum dolor sit amet lorem lorem</h1>
    <p>Lorem ipsum dolor sit amet, consectetur adipiscing elit, sed do eiusmod tempor incididunt ut labore et dolore magna aliqua ut enim ad minim.</p>
    <span class="btn">Read more</span>
  </div>
</section>

<h2 class="section-title">Featured Auctions
  <svg width="26" height="22" viewBox="0 0 26 22"><rect x="4" y="3" width="12" height="6" rx="1" fill="#e2404f" transform="rotate(-30 10 6)"/><rect x="11" y="8" width="3" height="12" fill="#e2404f" transform="rotate(-30 12 14)"/><rect x="2" y="19" width="12" height="3" fill="#e2404f"/></svg>
</h2>

<main class="auction-grid">
  <article class="auction-card">
    <div class="tag">Sealed bid real estate auction</div>
    <div class="thumb" role="img" aria-label="Photo of an auction property"></div>
    <h3>Sealed Bid Auction</h3>
    <p class="desc">Lorem ipsum dolor sit amet, consectetur adipiscing elit, sed do eiusmod tempor incididunt ut labore et dolore magna aliqua.</p>
    <div class="meta"><svg width="12" height="12" viewBox="0 0 12 12"><circle cx="6" cy="6" r="5" fill="none" stroke="#e2404f" stroke-width="1.5"/><path d="M6 3v3h2.5" stroke="#e2404f" stroke-width="1.5" fill="none"/></svg><b>Begins :</b><span>Wednesday, August 22, 2013<br>at 6:00 PM CST</span></div>
    <div class="meta"><svg width="12" height="14" viewBox="0 0 12 14"><path d="M6 0a5 5 0 0 0-5 5c0 4 5 9 5 9s5-5 5-9a5 5 0 0 0-5-5z" fill="#e2404f"/><circle cx="6" cy="5" r="2" fill="#fff"/></svg><b>Location :</b><span>Gordon Brennick Auction &amp; Realty<br>3817 Pelham Court<br>Castor Falls, IN 47088</span></div>
  </article>
  <article class="auction-card">
    <div class="tag">Sealed bid real estate auction</div>
    <div class="thumb" role="img" aria-label="Photo of an auction property"></div>
    <h3>Sealed Bid Auction</h3>
    <p class="desc">Lorem ipsum dolor sit amet, consectetur adipiscing elit, sed do eiusmod tempor incididunt ut labore et dolore magna aliqua.</p>
    <div class="meta"><svg width="12" height="12" viewBox="0 0 12 12"><circle cx="6" cy="6" r="5" fill="none" stroke="#e2404f" stroke-width="1.5"/><path d="M6 3v3h2.5" stroke="#e2404f" stroke-width="1.5" fill="none"/></svg><b>Begins :</b><span>Wednesday, August 22, 2013<br>at 6:00 PM CST</span></div>
    <div class="meta"><svg width="12" height="14" viewBox="0 0 12 14"><path d="M6 0a5 5 0 0 0-5 5c0 4 5 9 5 9s5-5 5-9a5 5 0 0 0-5-5z" fill="#e2404f"/><circle cx="6" cy="5" r="2" fill="#fff"/></svg><b>Location :</b><span>Gordon Brennick Auction &amp; Realty<br>3817 Pelham Court<br>Castor Falls, IN 47088</span></div>
  </article>
  <article class="auction-card">
    <div class="tag">Sealed bid real estate auction</div>
    <div class="thumb" role="img" aria-label="Photo of an auction property"></div>
    <h3>Sealed Bid Auction</h3>
    <p class="desc">Lorem ipsum dolor sit amet, consectetur adipiscing elit, sed do eiusmod tempor incididunt ut labore et dolore magna aliqua.</p>
    <div class="meta"><svg width="12" height="12" viewBox="0 0 12 12"><circle cx="6" cy="6" r="5" fill="none" stroke="#e2404f" stroke-width="1.5"/><path d="M6 3v3h2.5" stroke="#e2404f" stroke-width="1.5" fill="none"/></svg><b>Begins :</b><span>Wednesday, August 22, 2013<br>at 6:00 PM CST</span></div>
    <div class="meta"><svg width="12" height="14" viewBox="0 0 12 14"><path d="M6 0a5 5 0 0 0-5 5c0 4 5 9 5 9s5-5 5-9a5 5 0 0 0-5-5z" fill="#e2404f"/><circle cx="6" cy="5" r="2" fill="#fff"/></svg><b>Location :</b><span>Gordon Brennick Auction &amp; Realty<br>3817 Pelham Court<br>Castor Falls, IN 47088</span></div>
  </article>
  <article class="auction-card">
    <div class="tag">Sealed bid real estate auction</div>
    <div class="thumb" role="img" aria-label="Photo of an auction property"></div>
    <h3>Sealed Bid Auction</h3>
    <p class="desc">Lorem ipsum dolor sit amet, consectetur adipiscing elit, sed do eiusmod tempor incididunt ut labore et dolore magna aliqua.</p>
    <div class="meta"><svg width="12" height="12" viewBox="0 0 12 12"><circle cx="6" cy="6" r="5" fill="none" stroke="#e2404f" stroke-width="1.5"/><path d="M6 3v3h2.5" stroke="#e2404f" stroke-width="1.5" fill="none"/></svg><b>Begins :</b><span>Wednesday, August 22, 2013<br>at 6:00 PM CST</span></div>
    <div class="meta"><svg width="12" height="14" viewBox="0 0 12 14"><path d="M6 0a5 5 0 0 0-5 5c0 4 5 9 5 9s5-5 5-9a5 5 0 0 0-5-5z" fill="#e2404f"/><circle cx="6" cy="5" r="2" fill="#fff"/></svg><b>Location :</b><span>Gordon Brennick Auction &amp; Realty<br>3817 Pelham Court<br>Castor Falls, IN 47088</span></div>
  </article>
  <article class="auction-card">
    <div class="tag">Sealed bid real estate auction</div>
    <div class="thumb" role="img" aria-label="Photo of an auction property"></div>
    <h3>Sealed Bid Auction</h3>
    <p class="desc">Lorem ipsum dolor sit amet, consectetur adipiscing elit, sed do eiusmod tempor incididunt ut labore et dolore magna aliqua.</p>
    <div class="meta"><svg width="12" height="12" viewBox="0 0 12 12"><circle cx="6" cy="6" r="5" fill="none" stroke="#e2404f" stroke-width="1.5"/><path d="M6 3v3h2.5" stroke="#e2404f" stroke-width="1.5" fill="none"/></svg><b>Begins :</b><span>Wednesday, August 22, 2013<br>at 6:00 PM CST</span></div>
    <div class="meta"><svg width="12" height="14" viewBox="0 0 12 14"><path d="M6 0a5 5 0 0 0-5 5c0 4 5 9 5 9s5-5 5-9a5 5 0 0 0-5-5z" fill="#e2404f"/><circle cx="6" cy="5" r="2" fill="#fff"/></svg><b>Location :</b><span>Gordon Brennick Auction &amp; Realty<br>3817 Pelham Court<br>Castor Falls, IN 47088</span></div>
  </article>
  <article class="auction-card">
    <div class="tag">Sealed bid real estate auction</div>
    <div class="thumb" role="img" aria-label="Photo of an auction property"></div>
    <h3>Sealed Bid Auction</h3>
    <p class="desc">Lorem ipsum dolor sit amet, consectetur adipiscing elit, sed do eiusmod tempor incididunt ut labore et dolore magna aliqua.</p>
    <div class="meta"><svg width="12" height="12" viewBox="0 0 12 12"><circle cx="6" cy="6" r="5" fill="none" stroke="#e2404f" stroke-width="1.5"/><path d="M6 3v3h2.5" stroke="#e2404f" stroke-width="1.5" fill="none"/></svg><b>Begins :</b><span>Wednesday, August 22, 2013<br>at 6:00 PM CST</span></div>
    <div class="meta"><svg width="12" height="14" viewBox="0 0 12 14"><path d="M6 0a5 5 0 0 0-5 5c0 4 5 9 5 9s5-5 5-9a5 5 0 0 0-5-5z" fill="#e2404f"/><circle cx="6" cy="5" r="2" fill="#fff"/></svg><b>Location :</b><span>Gordon Brennick Auction &amp; Realty<br>3817 Pelham Court<br>Castor Falls, IN 47088</span></div>
  </article>
  <article class="auction-card">
    <div class="tag">Sealed bid real estate auction</div>
    <div class="thumb" role="img" aria-label="Photo of an auction property"></div>
    <h3>Sealed Bid Auction</h3>
    <p class="desc">Lorem ipsum dolor sit amet, consectetur adipiscing elit, sed do eiusmod tempor incididunt ut labore et dolore magna aliqua.</p>
    <div class="meta"><svg width="12" height="12" viewBox="0 0 12 12"><circle cx="6" cy="6" r="5" fill="none" stroke="#e2404f" stroke-width="1.5"/><path d="M6 3v3h2.5" stroke="#e2404f" stroke-width="1.5" fill="none"/></svg><b>Begins :</b><span>Wednesday, August 22, 2013<br>at 6:00 PM CST</span></div>
    <div class="meta"><svg width="12" height="14" viewBox="0 0 12 14"><path d="M6 0a5 5 0 0 0-5 5c0 4 5 9 5 9s5-5 5-9a5 5 0 0 0-5-5z" fill="#e2404f"/><circle cx="6" cy="5" r="2" fill="#fff"/></svg><b>Location :</b><span>Gordon Brennick Auction &amp; Realty<br>3817 Pelham Court<br>Castor Falls, IN 47088</span></div>
  </article>
  <article class="auction-card">
    <div class="tag">Sealed bid real estate auction</div>
    <div class="thumb" role="img" aria-label="Photo of an auction property"></div>
    <h3>Sealed Bid Auction</h3>
    <p class="desc">Lorem ipsum dolor sit amet, consectetur adipiscing elit, sed do eiusmod tempor incididunt ut labore et dolore magna aliqua.</p>
    <div class="meta"><svg width="12" height="12" viewBox="0 0 12 12"><circle cx="6" cy="6" r="5" fill="none" stroke="#e2404f" stroke-width="1.5"/><path d="M6 3v3h2.5" stroke="#e2404f" stroke-width="1.5" fill="none"/></svg><b>Begins :</b><span>Wednesday, August 22, 2013<br>at 6:00 PM CST</span></div>
    <div class="meta"><svg width="12" height="14" viewBox="0 0 12 14"><path d="M6 0a5 5 0 0 0-5 5c0 4 5 9 5 9s5-5 5-9a5 5 0 0 0-5-5z" fill="#e2404f"/><circle cx="6" cy="5" r="2" fill="#fff"/></svg><b>Location :</b><span>Gordon Brennick Auction &amp; Realty<br>3817 Pelham Court<br>Castor Falls, IN 47088</span></div>
  </article>
</main>

<aside class="sidebar">
  <section class="widget">
    <h4>Newsletter Sign Up</h4>
    <div class="body">Lorem ipsum dolor sit amet, consectetur adipiscing elit, sed do eiusmod tempor.
      <div class="field"></div>
      <div class="subscribe">SUBSCRIBE</div>
    </div>
  </section>
  <section class="widget">
    <h4>Social Media</h4>
    <div class="body"><div class="social-row"><span>Like</span><span>Follow</span><span>Watch</span></div></div>
  </section>
  <section class="widget">
    <h4>News</h4>
    <div class="body">
      <div class="item"><div class="date">19<br>Aug</div><div><strong>Lorem ipsum dolor sit amet</strong>Consectetur adipiscing elit, sed do eiusmod tempor incididunt.</div></div>
      <div class="item"><div class="date">19<br>Aug</div><div><strong>Lorem ipsum dolor sit amet</strong>Consectetur adipiscing elit, sed do eiusmod tempor incididunt.</div></div>
      <div class="view-all">VIEW ALL</div>
    </div>
  </section>
  <section class="widget">
    <h4>Events Blog</h4>
    <div class="body">
      <div class="item"><div class="avatar" role="img" aria-label="Portrait photo"></div><div><strong>Lorem ipsum dolor sit amet</strong>Consectetur adipiscing elit, sed do eiusmod tempor incididunt.</div></div>
      <div class="item"><div class="avatar" role="img" aria-label="Portrait photo"></div><div><strong>Lorem ipsum dolor sit amet</strong>Consectetur adipiscing elit, sed do eiusmod tempor incididunt.</div></div>
      <div class="view-all">VIEW ALL</div>
    </div>
  </section>
  <section class="widget">
    <h4>Testimonials</h4>
    <div class="body">
      <div class="item"><div class="avatar" role="img" aria-label="Portrait photo"></div><div><strong>Lorem ipsum dolor sit amet</strong>Consectetur adipiscing elit, sed do eiusmod tempor incididunt.</div></div>
      <div class="item"><div class="avatar" role="img" aria-label="Portrait photo"></div><div><strong>Lorem ipsum dolor sit amet</strong>Consectetur adipiscing elit, sed do eiusmod tempor incididunt.</div></div>
      <div class="view-all">VIEW ALL</div>
    </div>
  </section>
  <section class="widget">
    <h4>Featured Auctions</h4>
    <div class="body">
      <div class="pics"><div role="img" aria-label="Photo of a featured auction house"></div><div role="img" aria-label="Photo of a featured auction house"></div></div>
      <div class="view-all" style="margin-top:10px">VIEW ALL</div>
    </div>
  </section>
  <section class="widget">
    <h4>Featured Listings</h4>
    <div class="body">
      <div class="pics"><div role="img" aria-label="Photo of a listed property"></div><div role="img" aria-label="Photo of a listed property"></div></div>
      <div class="view-all" style="margin-top:10px">VIEW ALL</div>
    </div>
  </section>
</aside>

<section class="brand-band">
  <div class="brand">brennickauctions.example</div>
  <div class="partners"><i></i><i></i><i></i><i></i></div>
</section>

<footer class="site-footer">
  <div class="contacts">
    <span><svg width="20" height="20" viewBox="0 0 20 20"><path d="M4 1h4l2 5-3 2a11 11 0 0 0 5 5l2-3 5 2v4a2 2 0 0 1-2 2A17 17 0 0 1 2 3a2 2 0 0 1 2-2z" fill="#e2404f"/></svg>812.555.0146</span>
    <span><svg width="20" height="20" viewBox="0 0 20 20"><path d="M4 1h4l2 5-3 2a11 11 0 0 0 5 5l2-3 5 2v4a2 2 0 0 1-2 2A17 17 0 0 1 2 3a2 2 0 0 1 2-2z" fill="#e2404f"/></svg>877.555.0193</span>
    <span><svg width="22" height="16" viewBox="0 0 22 16"><rect x="1" y="1" width="20" height="14" fill="none" stroke="#e2404f" stroke-width="2"/><path d="M1 1l10 8 10-8" fill="none" stroke="#e2404f" stroke-width="2"/></svg>dominic@brennickauctions.example</span>
  </div>
  <p class="address"><b>Gordon Brennick Auction-Realty</b>3817 Pelham Court, Castor Falls, IN 47088</p>
  <div class="legal">© 2013 Brennick Auction. All rights reserved.</div>
</footer>
</body>
</html>
```